KiteSurf Weather App Forecast Screen re-design (1 Screen)

We are redesigning our application, BreezeLoom. Our main screen is the forecast screen. The forecast screen presents the forecast for multiple places for the selected day.

Intro
-----

The user has a list of favorite spots that he is monitoring. Then he selects the date that he wants to get the forecast. The forecast screen presents a list of all the spots and a summary of the weather conditions. Spots are sorted by weather conditions. At the top, he gets the spot with the best weather conditions. We have an algorithm that can evaluate whether given weather conditions are good or not. When they are good we indicate that to the user.

Current Solution
------------------

There is also a landscape version, which contains a bit more data: "Current Forecast Screen Lanscape.jpeg". The landscape one is a bit funny, as it is taken from an Zentra Q and the app was not designed for it at the time.

The bars that you see for each hour use our algorithm to display whether the conditions are good:

- When the color is gray the conditions are not good
- When the color is yellow there are light wind conditions
- When the color is green there are good
- When the color is red the wind is very strong
- The height of the bar indicates wind strength

More Info
-----------

The detailed forecast screen is also attached so you can get a bit more context, "DetailedForecast.jpeg"

An example from an application that has a similar chart is attached, "SimilarApp.jpeg". I have circled the chart with red.

Future Solution
------------------

(See note.jpeg)

We want to create a page that contains more information and passes a better message to our users.

The elements that are important and we want to present to the user are the following:

1. Wind. (The most important)
It contains two elements: strength and direction.

1.1 Wind Strength.
Good wind strength is anything between 10-45 knots (measurement unit like km/h). The best representation with a color palette.
Gray will be the color used when the strength is not between 10-45.
The palette should start with yellow at 10 knots, then move toward green for 22knots and finally go towards red for 45 knots.

1.2 Wind Direction.
There are good wind directions that we can kite and directions that is is not possible.
Can be presented by an arrow that points in the direction the wind is blowing to. The color of the arrow will be green when the direction is good, yellow when it is average and gray when it is not good.

My thought for portrait mode is to use an arrow point for the direction and the color of the arrow to represent the strength. Solution number 2 on my notes. Then for landscape, we could use both a number and an arrow like number 4 on my notes.

2. Wave.
It contains three elements: height, period and direction. It is not displayed to all of our users only the ones that have selected the wave riding option.

2.1 Height is represented by a number. Ex. 1.2 meters or 2 foot.
2.2 Period is represented in seconds. Ex. 12 seconds.
2.3 Directions is an arrow that points to the direction the wave is coming from.

Again the solution should be like the wind. Arrow for direction and the color of the arrow for height. The palette here should be something with different blue colors.

3. Tide height. (Optional for tidal spots, as not all spots have tides)

The best way to represent that it through a graph. I would also like to see an alternative, where we have three symbols for low, mid and high tide.

4. General Weather. Rain/Snow and temperature.

This should be represented by a sun/cloud/rain symbol. If it is very cold the symbol can also contain an ice sign on the background.

---------

This is a guideline creativity will be valued. Maybe there is another way to do it that I have not thought about.

The winner of the competition will have to send us all graphics used in vector format, so we can input them to our xCode project.

Finally the person that wins the competition will be the first one to be considered for the redesign of the rest of our application.

Target Market(s)

Kitesurfers

Font styles to use
Sans Serif

Colors

Designer to choose colors to be used in the design.

Requirements
Must have
• It should be minimal and clearly communicate the weather forecast to my users. It should be user friendly.
Nice to have
• Communicative color palettes for both wind strength, tide and waves
Should not have
• Hard to understand UI

```html
<!DOCTYPE html>
<html lang="en">
<head>
<meta charset="utf-8">
<title>BreezeLoom – My Favorites</title>
<link href="https://fonts.googleapis.com/css2?family=Montserrat:wght@400;500;600&display=swap" rel="stylesheet">
<style>
  :root {
    --canvas: #e9edf2;
    --navy-deep: #0a2766;
    --navy: #0c3479;
    --blue-row: #0f4793;
    --blue-row-alt: #0e4a98;
    --blue-spot: #135aa9;
    --blue-fade: #0b3a86;
    --tab-bar: #0c2f6c;
    --divider: rgba(255,255,255,0.07);
    --text: #ffffff;
    --muted: #8fa7cf;
    --sun: #f2e52c;
    --light-wind: #f5ea1d;
    --good: #48ec77;
    --strong: #e8494a;
    --calm: #8796b5;
    --trend: #6c9ce0;
    --cloud: #b9c9e6;
  }
  * { margin: 0; padding: 0; box-sizing: border-box; }
  html, body {
    width: 837px; height: 1200px; overflow: hidden;
    background: var(--canvas);
    font-family: "Montserrat", sans-serif;
    color: var(--text);
  }
  .screen {
    position: absolute; left: 80px; top: 0;
    width: 677px; height: 1200px; overflow: hidden;
    background: linear-gradient(180deg, var(--navy-deep) 0%, var(--blue-row) 45%, var(--blue-spot) 60%, var(--blue-fade) 92%);
  }
  .status-bar {
    position: absolute; top: 0; left: 0; right: 0; height: 45px;
    font-size: 19px; font-weight: 500;
  }
  .status-bar .carrier { position: absolute; left: 22px; top: 11px; display: flex; align-items: center; gap: 6px; }
  .status-bar .clock { position: absolute; left: 0; right: 0; top: 11px; text-align: center; }
  .status-bar .power { position: absolute; right: 22px; top: 11px; display: flex; align-items: center; gap: 8px; }
  .nav-bar { position: absolute; top: 45px; left: 0; right: 0; height: 109px; background: var(--navy-deep); }
  .status-bar + .nav-bar { z-index: 0; }
  .header-band { position: absolute; top: 0; left: 0; right: 0; height: 154px; background: var(--navy-deep); }
  .nav-title { position: absolute; top: 81px; left: 0; right: 0; text-align: center; font-size: 21px; font-weight: 500; }
  .menu-button { position: absolute; left: 580px; top: 76px; }

  .spot-header { position: absolute; left: 0; right: 0; height: 175px; }
  .spot-header.is-best { top: 154px; background: var(--navy); }
  .spot-header.is-second { top: 573px; background: var(--blue-spot); }
  .spot-name { position: absolute; left: 46px; top: 18px; font-size: 35px; font-weight: 500; letter-spacing: 0.2px; }
  .hour-icons { position: absolute; left: 0; top: 72px; }
  .hours {
    position: absolute; left: 77px; top: 124px; width: 532px;
    display: grid; grid-template-columns: repeat(11, 1fr);
    font-size: 19px; font-weight: 500; text-align: center;
  }

  .data-row { position: absolute; left: 0; right: 0; border-top: 1px solid var(--divider); }
  .data-row .row-label { position: absolute; left: 38px; font-size: 15px; color: var(--muted); font-weight: 500; }
  .row-strength { height: 84px; background: var(--blue-row); }
  .row-direction { height: 79px; background: var(--blue-row-alt); }
  .row-temperature { height: 81px; background: var(--blue-row); }
  .row-strength .row-label { top: 50px; }
  .row-direction .row-label { top: 29px; }
  .row-temperature .row-label { top: 26px; }
  .data-row svg { position: absolute; left: 0; top: 0; }

  .tab-bar {
    position: absolute; left: 0; right: 0; bottom: 0; height: 90px;
    background: var(--tab-bar);
  }
  .tab-bar svg { position: absolute; top: 22px; }
</style>
</head>
<body>
<svg width="0" height="0" style="position:absolute">
  <defs>
    <symbol id="icon-sun" viewBox="-14 -14 28 28">
      <g fill="none" stroke="#f2e52c" stroke-width="1.6" stroke-linecap="round">
        <circle r="5.5"/>
        <path d="M0 -9V-12M0 9V12M-9 0H-12M9 0H12M6.4 -6.4L8.5 -8.5M-6.4 6.4L-8.5 8.5M6.4 6.4L8.5 8.5M-6.4 -6.4L-8.5 -8.5"/>
      </g>
    </symbol>
    <symbol id="icon-partly-cloudy" viewBox="-16 -14 32 28">
      <g fill="none" stroke="#b9c9e6" stroke-width="1.4" stroke-linecap="round">
        <path d="M-12 9H8a5 5 0 0 0 0-10 7 7 0 0 0-13-1 5 5 0 0 0-7 11z"/>
        <circle cx="6" cy="-5" r="3.5"/>
        <path d="M6 -11.5V-13M11.5 -5H13M10 -9.5L11 -10.5M1.5 -9.5L0.5 -10.5"/>
      </g>
    </symbol>
    <symbol id="icon-wind" viewBox="-14 -12 28 24">
      <g fill="none" stroke="#7e8fb6" stroke-width="1.4" stroke-linecap="round">
        <path d="M-11 -3H6a3.5 3.5 0 1 0-3.5-3.5"/>
        <path d="M-11 2H9a3.5 3.5 0 1 1-3.5 3.5"/>
        <path d="M-8 -7.5H0"/>
      </g>
    </symbol>
    <symbol id="dir-arrow" viewBox="-12 -12 24 24" overflow="visible">
      <path d="M10 0L-8 -7.5L-3.5 0L-8 7.5Z"/>
    </symbol>
  </defs>
</svg>

<main class="screen">
  <div class="header-band"></div>

  <div class="status-bar">
    <div class="carrier">
      <svg width="58" height="12" viewBox="0 0 58 12">
        <g fill="#fff"><circle cx="6" cy="6" r="5"/><circle cx="18" cy="6" r="5"/><circle cx="30" cy="6" r="5"/></g>
        <g fill="none" stroke="#fff" stroke-width="1.2"><circle cx="42" cy="6" r="4.4"/><circle cx="54" cy="6" r="3.4"/></g>
      </svg>
      <span>Nova</span>
      <svg width="20" height="16" viewBox="0 0 20 16"><g fill="none" stroke="#fff" stroke-width="2" stroke-linecap="round"><path d="M2 6a11 11 0 0 1 16 0"/><path d="M5 9.5a6.5 6.5 0 0 1 10 0"/></g><circle cx="10" cy="13" r="1.8" fill="#fff"/></svg>
    </div>
    <div class="clock">4:21 PM</div>
    <div class="power">
      <svg width="12" height="20" viewBox="0 0 12 20"><path d="M1 5l9 9-4.5 4.5V1.5L10 6l-9 9" fill="none" stroke="#c9d3e8" stroke-width="1.4"/></svg>
      <span>100%</span>
      <svg width="42" height="18" viewBox="0 0 42 18"><rect x="1" y="1.5" width="36" height="15" rx="3" fill="none" stroke="#fff" stroke-width="1.4"/><rect x="3.5" y="4" width="31" height="10" rx="1.5" fill="#fff"/><rect x="38.5" y="6" width="2.5" height="6" rx="1" fill="#fff"/></svg>
    </div>
  </div>

  <h1 class="nav-title">My Favorites</h1>
  <svg class="menu-button" width="46" height="30" viewBox="0 0 46 30" aria-label="Menu">
    <g stroke="#fff" stroke-width="3"><path d="M1 2H45M1 15H45M1 28H45"/></g>
  </svg>

  <!-- Spot 1 -->
  <section class="spot-header is-best">
    <h2 class="spot-name">Cape Town</h2>
    <svg class="hour-icons" width="677" height="40" viewBox="0 0 677 40">
      <use href="#icon-partly-cloudy" x="85" y="6" width="32" height="28"/>
      <use href="#icon-partly-cloudy" x="127" y="6" width="32" height="28"/>
      <use href="#icon-sun" x="176" y="6" width="28" height="28"/>
      <use href="#icon-sun" x="225" y="6" width="28" height="28"/>
      <use href="#icon-sun" x="271" y="6" width="28" height="28"/>
      <use href="#icon-sun" x="321" y="6" width="28" height="28"/>
      <use href="#icon-sun" x="371" y="6" width="28" height="28"/>
      <use href="#icon-sun" x="422" y="6" width="28" height="28"/>
      <use href="#icon-wind" x="472" y="8" width="28" height="24"/>
      <use href="#icon-wind" x="522" y="8" width="28" height="24"/>
      <use href="#icon-wind" x="571" y="8" width="28" height="24"/>
    </svg>
    <div class="hours"><span>8</span><span>9</span><span>10</span><span>11</span><span>12</span><span>13</span><span>14</span><span>15</span><span>16</span><span>17</span><span>18</span></div>
  </section>

  <section class="data-row row-strength" style="top:329px">
    <span class="row-label">W</span>
    <svg width="677" height="84" viewBox="0 0 677 84" aria-label="Wind strength by hour">
      <path d="M81 59H598" stroke="#8a9bc0" stroke-width="1.2"/>
      <path d="M81 59V53H110V51H135V52H150V49H165V50H190V48H205V46H220V50H245V51H270V59Z" fill="var(--light-wind)"/>
      <path d="M270 59V34H285V32H300V30H315V33H330V31H345V29H360V32H375V34H395V39H410V44H420V59Z" fill="var(--good)"/>
      <path d="M528 59V35H550V27H570V15H598V59Z" fill="var(--strong)"/>
    </svg>
  </section>

  <section class="data-row row-direction" style="top:413px">
    <span class="row-label">W</span>
    <svg width="677" height="79" viewBox="0 0 677 79" aria-label="Wind direction by hour">
      <g fill="var(--good)">
        <use href="#dir-arrow" x="89" y="28" width="24" height="24" transform="rotate(-50 101 40)"/>
        <use href="#dir-arrow" x="131" y="28" width="24" height="24" transform="rotate(-50 143 40)"/>
        <use href="#dir-arrow" x="178" y="28" width="24" height="24" transform="rotate(-50 190 40)"/>
        <use href="#dir-arrow" x="227" y="28" width="24" height="24" transform="rotate(-50 239 40)"/>
        <use href="#dir-arrow" x="273" y="28" width="24" height="24" transform="rotate(-50 285 40)"/>
        <use href="#dir-arrow" x="323" y="28" width="24" height="24" transform="rotate(-55 335 40)"/>
        <use href="#dir-arrow" x="373" y="28" width="24" height="24" transform="rotate(-50 385 40)"/>
      </g>
      <g fill="var(--light-wind)">
        <use href="#dir-arrow" x="424" y="28" width="24" height="24" transform="rotate(5 436 40)"/>
        <use href="#dir-arrow" x="474" y="28" width="24" height="24" transform="rotate(0 486 40)"/>
      </g>
      <g fill="var(--calm)">
        <use href="#dir-arrow" x="524" y="28" width="24" height="24" transform="rotate(-120 536 40)"/>
        <use href="#dir-arrow" x="573" y="28" width="24" height="24" transform="rotate(-140 585 40)"/>
      </g>
    </svg>
  </section>

  <section class="data-row row-temperature" style="top:492px">
    <span class="row-label">T</span>
    <svg width="677" height="81" viewBox="0 0 677 81" aria-label="Temperature trend">
      <polyline fill="none" stroke="var(--trend)" stroke-width="1.5" stroke-linejoin="round" points="87,45 100,25 113,45 126,28 140,31 153,30 167,33 180,27 193,35 206,26 220,45 233,25 246,45 260,27 273,44 286,26 300,34 313,30 327,32 340,29 353,33 367,28 380,45 393,26 406,45 420,32 433,34 446,27 460,45 473,25 487,38 500,33 513,35 527,44 540,43 553,26 567,45 579,25"/>
    </svg>
  </section>

  <!-- Spot 2 -->
  <section class="spot-header is-second">
    <h2 class="spot-name">Loutsa</h2>
    <svg class="hour-icons" width="677" height="40" viewBox="0 0 677 40">
      <use href="#icon-partly-cloudy" x="85" y="6" width="32" height="28"/>
      <use href="#icon-partly-cloudy" x="127" y="6" width="32" height="28"/>
      <use href="#icon-sun" x="176" y="6" width="28" height="28"/>
      <use href="#icon-sun" x="225" y="6" width="28" height="28"/>
      <use href="#icon-sun" x="271" y="6" width="28" height="28"/>
      <use href="#icon-sun" x="321" y="6" width="28" height="28"/>
      <use href="#icon-sun" x="371" y="6" width="28" height="28"/>
      <use href="#icon-sun" x="422" y="6" width="28" height="28"/>
      <use href="#icon-wind" x="472" y="8" width="28" height="24"/>
      <use href="#icon-wind" x="522" y="8" width="28" height="24"/>
      <use href="#icon-wind" x="571" y="8" width="28" height="24"/>
    </svg>
    <div class="hours"><span>8</span><span>9</span><span>10</span><span>11</span><span>12</span><span>13</span><span>14</span><span>15</span><span>16</span><span>17</span><span>18</span></div>
  </section>

  <section class="data-row row-strength" style="top:747px">
    <span class="row-label">W</span>
    <svg width="677" height="84" viewBox="0 0 677 84" aria-label="Wind strength by hour">
      <path d="M81 61H598" stroke="#8a9bc0" stroke-width="1.2"/>
      <path d="M81 61V55H110V53H122V54H135V50H150V53H160V50H172V56H190V48H205V51H230V52H270V61Z" fill="var(--light-wind)"/>
      <path d="M270 61V44H285V36H295V32H305V28H315V38H330V34H345V30H360V34H370V42H380V36H395V46H410V49H420V61Z" fill="var(--good)"/>
      <path d="M528 61V42H540V52H548V34H560V46H570V24H580V42H588V16H598V61Z" fill="var(--strong)"/>
    </svg>
  </section>

  <section class="data-row row-direction" style="top:832px">
    <span class="row-label">W</span>
    <svg width="677" height="80" viewBox="0 0 677 80" aria-label="Wind direction by hour">
      <g fill="var(--good)">
        <use href="#dir-arrow" x="89" y="29" width="24" height="24" transform="rotate(-50 101 41)"/>
        <use href="#dir-arrow" x="131" y="29" width="24" height="24" transform="rotate(-50 143 41)"/>
        <use href="#dir-arrow" x="178" y="29" width="24" height="24" transform="rotate(-50 190 41)"/>
        <use href="#dir-arrow" x="227" y="29" width="24" height="24" transform="rotate(-50 239 41)"/>
        <use href="#dir-arrow" x="273" y="29" width="24" height="24" transform="rotate(-50 285 41)"/>
        <use href="#dir-arrow" x="323" y="29" width="24" height="24" transform="rotate(-55 335 41)"/>
        <use href="#dir-arrow" x="373" y="29" width="24" height="24" transform="rotate(-50 385 41)"/>
      </g>
      <g fill="var(--light-wind)">
        <use href="#dir-arrow" x="424" y="29" width="24" height="24" transform="rotate(5 436 41)"/>
        <use href="#dir-arrow" x="474" y="29" width="24" height="24" transform="rotate(0 486 41)"/>
      </g>
      <g fill="var(--calm)">
        <use href="#dir-arrow" x="524" y="29" width="24" height="24" transform="rotate(-120 536 41)"/>
        <use href="#dir-arrow" x="573" y="29" width="24" height="24" transform="rotate(-140 585 41)"/>
      </g>
    </svg>
  </section>

  <section class="data-row row-temperature" style="top:912px; background:transparent">
    <span class="row-label">T</span>
    <svg width="677" height="81" viewBox="0 0 677 81" aria-label="Temperature trend">
      <polyline fill="none" stroke="var(--trend)" stroke-width="1.5" stroke-linejoin="round" points="87,45 100,25 113,45 126,28 140,31 153,30 167,33 180,27 193,35 206,26 220,45 233,25 246,45 260,27 273,44 286,26 300,34 313,30 327,32 340,29 353,33 367,28 380,45 393,26 406,45 420,32 433,34 446,27 460,45 473,25 487,38 500,33 513,35 527,44 540,43 553,26 567,45 579,25"/>
    </svg>
  </section>

  <nav class="tab-bar">
    <svg style="left:103px" width="46" height="54" viewBox="0 0 46 54" aria-label="Profile">
      <g fill="none" stroke="#8fa7cf" stroke-width="2"><circle cx="23" cy="15" r="11"/><path d="M3 50c0-11 8-18 20-18s20 7 20 18z" stroke-linejoin="round"/></g>
    </svg>
    <svg style="left:318px" width="54" height="48" viewBox="0 0 54 48" aria-label="Favorites">
      <path d="M27 45L6 24C-1 17 3 3 14 3c6 0 10 4 13 8 3-4 7-8 13-8 11 0 15 14 8 21z" fill="none" stroke="#8fa7cf" stroke-width="2" stroke-linejoin="round"/>
    </svg>
    <svg style="left:532px" width="52" height="52" viewBox="-26 -26 52 52" aria-label="Settings">
      <g fill="none" stroke="#8fa7cf" stroke-width="2" stroke-linejoin="round">
        <path d="M-4 -23H4L5 -17L10 -14L16 -17L21 -11L17 -6L18 0L17 6L21 11L16 17L10 14L5 17L4 23H-4L-5 17L-10 14L-16 17L-21 11L-17 6L-18 0L-17 -6L-21 -11L-16 -17L-10 -14L-5 -17Z"/>
        <circle r="8"/>
      </g>
    </svg>
  </nav>
</main>
</body>
</html>
```